Commercial Construction Company

We need a business card design based on our current logo. We are a commercial general contractor based in Southern California that specializes in bank remodels. We would like to see designs that incorporate dark blue. The final design should portray an image of professionalism and quality.

If possible, I would like to add metallic foil to the design. Thank you

```html
<!DOCTYPE html>
<html lang="en">
<head>
<meta charset="utf-8">
<title>Halden Commercial Building Services – Business Card</title>
<link rel="stylesheet" href="https://fonts.googleapis.com/css2?family=Oswald:wght@500;600&family=Jost:wght@400&display=swap">
<style>
  :root{
    --navy:#0b4078;
    --navy-deep:#083562;
    --white:#ffffff;
    --ink:#151515;
    --stage:#e4e5e8;
    --foil-light:#f2f3f5;
    --foil-mid:#b9bcc1;
    --foil-dark:#8a8d93;
  }
  *{box-sizing:border-box;margin:0;padding:0}
  html,body{width:1200px;height:737px;overflow:hidden}
  body{background:var(--stage);position:relative;font-family:"Jost",sans-serif}
  .card{position:absolute;top:193px;width:523px;height:350px;background:var(--white);overflow:hidden;box-shadow:0 2px 6px rgba(0,0,0,.12)}
  .card--front{left:54px}
  .card--back{left:623px}
  .card__art{position:absolute;inset:0;width:100%;height:100%}
  .brand-mark{position:absolute;display:flex;align-items:center;gap:12px;transform:translate(-50%,-50%)}
  .brand-mark__dot{width:30px;height:30px;border-radius:50%;background:var(--navy)}
  .brand-mark__name{font-family:"Oswald",sans-serif;font-weight:600;font-size:50px;letter-spacing:1px;color:var(--ink);line-height:1}
  .card--front .brand-mark{left:272px;top:168px}
  .card--back .brand-mark{left:142px;top:168px}
  .company-pill{position:absolute;left:303px;top:56px;width:193px;height:64px;border-radius:20px;background:var(--white);
    display:flex;align-items:center;justify-content:center;text-align:center;
    font-family:"Oswald",sans-serif;font-weight:500;font-size:16.5px;line-height:19px;color:var(--navy);letter-spacing:.3px}
  .contact-list{position:absolute;left:322px;top:160px;list-style:none;color:var(--white);font-size:14px;line-height:19px}
  .contact-list::before{content:"";position:absolute;left:10px;top:12px;width:1px;height:150px;background:var(--white)}
  .contact-item{position:relative;display:flex;align-items:flex-start;gap:16px}
  .contact-item--phone{margin-top:0}
  .contact-item--email{margin-top:23px}
  .contact-item--address{margin-top:22px}
  .contact-icon{flex:0 0 21px;width:21px;height:21px;border-radius:4px;background:var(--white);display:flex;align-items:center;justify-content:center;position:relative;z-index:1}
  .contact-icon svg{width:12px;height:12px;fill:var(--navy)}
  .contact-text{padding-top:1px}
</style>
</head>
<body>

<section class="card card--front" aria-label="Business card front">
  <svg class="card__art" viewBox="0 0 523 350" aria-hidden="true">
    <defs>
      <linearGradient id="foil-front" x1="0" y1="0" x2="1" y2="1">
        <stop offset="0" stop-color="var(--foil-light)"/>
        <stop offset=".45" stop-color="var(--foil-dark)"/>
        <stop offset=".6" stop-color="var(--foil-light)"/>
        <stop offset="1" stop-color="var(--foil-mid)"/>
      </linearGradient>
    </defs>
    <polygon points="0,0 212,0 0,172" fill="var(--navy)"/>
    <polygon points="218,0 248,0 95,126 78,126" fill="url(#foil-front)"/>
    <polygon points="523,175 523,350 312,350" fill="var(--navy)"/>
    <polygon points="455,198 478,196 318,350 292,350" fill="url(#foil-front)"/>
  </svg>
  <div class="brand-mark">
    <span class="brand-mark__dot"></span>
    <span class="brand-mark__name">HCBS</span>
  </div>
</section>

<section class="card card--back" aria-label="Business card back">
  <svg class="card__art" viewBox="0 0 523 350" aria-hidden="true">
    <defs>
      <linearGradient id="foil-back" x1="0" y1="0" x2="1" y2="0">
        <stop offset="0" stop-color="var(--foil-dark)"/>
        <stop offset=".4" stop-color="var(--foil-light)"/>
        <stop offset=".75" stop-color="var(--foil-mid)"/>
        <stop offset="1" stop-color="var(--foil-dark)"/>
      </linearGradient>
    </defs>
    <path d="M160,0 H285 C262,0 252,15 255,40 C260,70 290,120 300,170 C320,240 280,300 215,350 H168 C250,290 287,230 276,165 C265,95 215,40 160,0 Z" fill="url(#foil-back)"/>
    <path d="M285,0 H523 V350 H215 C280,300 320,240 300,170 C290,120 260,70 255,40 C252,15 262,0 285,0 Z" fill="var(--navy)"/>
  </svg>
  <div class="brand-mark">
    <span class="brand-mark__dot"></span>
    <span class="brand-mark__name">HCBS</span>
  </div>
  <div class="company-pill">HALDEN COMMERCIAL<br>BUILDING SERVICES</div>
  <ul class="contact-list">
    <li class="contact-item contact-item--phone">
      <span class="contact-icon"><svg viewBox="0 0 24 24"><path d="M6.6 10.8a15.1 15.1 0 0 0 6.6 6.6l2.2-2.2a1 1 0 0 1 1-.25 11.4 11.4 0 0 0 3.6.57 1 1 0 0 1 1 1V20a1 1 0 0 1-1 1A17 17 0 0 1 3 4a1 1 0 0 1 1-1h3.5a1 1 0 0 1 1 1c0 1.25.2 2.45.57 3.57a1 1 0 0 1-.25 1z"/></svg></span>
      <span class="contact-text">(909) 555-0142<br>(833) 555-0178</span>
    </li>
    <li class="contact-item contact-item--email">
      <span class="contact-icon"><svg viewBox="0 0 24 24"><path d="M2 5h20v14H2z M3.5 6.5 12 13l8.5-6.5" fill="none" stroke="var(--navy)" stroke-width="2"/><path d="M3 6h18l-9 7z"/></svg></span>
      <span class="contact-text">info@haldencbs.com</span>
    </li>
    <li class="contact-item contact-item--address">
      <span class="contact-icon"><svg viewBox="0 0 24 24"><path d="M12 2a7 7 0 0 0-7 7c0 5.2 7 13 7 13s7-7.8 7-13a7 7 0 0 0-7-7zm0 9.5A2.5 2.5 0 1 1 12 6.5a2.5 2.5 0 0 1 0 5z"/></svg></span>
      <span class="contact-text">4120 Meridian Park<br>Drive, Suite 310<br>Larkspur Vale,<br>CA 91700</span>
    </li>
  </ul>
</section>

</body>
</html>
```